Agricultural Consulting Website

Provide a modern yet business like website for my new Agriculture Consulting Business in Australia called FieldNorth. Whilst we are based in Australia we are targetting both domestic and international markets (especially in Asia). We are targetting corporate, small business, government and farmer clients. The design should compliment our logo also sourced through pixel harbor. The webiste should be easy for me to keep updated on a regular basis without the need to go back to the designer.

Industry/Entity Type

Business

Requirements
Must have
• clean crisp feel
• be modern yet business like
• be able to be updated by myself easily

```html
<!DOCTYPE html>
<html lang="en">
<head>
<meta charset="utf-8">
<title>FieldNorth — Agricultural Consulting</title>
<link href="https://fonts.googleapis.com/css2?family=Lato:ital,wght@0,400;0,700;1,400&family=Mulish:wght@700;800&display=swap" rel="stylesheet">
<style>
:root{
  --sky:#2fa7ea;
  --sky-light:#8fd3f6;
  --grass:#3f9a12;
  --grass-light:#8fd14a;
  --page:#ffffff;
  --paper:#f3f3f3;
  --green:#5f9b00;
  --green-dark:#4d8100;
  --brown:#6a3a0c;
  --text:#2b2b2b;
  --muted:#555;
  --dark:#1b1b1b;
}
*{margin:0;padding:0;box-sizing:border-box}
html,body{width:1200px;height:2224px;overflow:hidden}
body{position:relative;background:var(--paper);font-family:"Lato",sans-serif;color:var(--text)}
.abs{position:absolute}
.sky{left:0;top:0;width:1200px;height:650px;background:linear-gradient(180deg,var(--sky) 0%,var(--sky-light) 100%)}
.grass{top:380px;width:120px;height:270px;background:linear-gradient(180deg,var(--grass-light),var(--grass))}
.grass.left{left:0}
.grass.right{right:0}
.page{left:55px;top:64px;width:1088px;height:2083px;background:var(--page);box-shadow:0 0 6px rgba(0,0,0,.15)}

.brand{left:73px;top:79px;display:flex;align-items:center;gap:14px}
.brand-mark{width:92px;height:92px;background:var(--green-dark)}
.brand-name{font-family:"Lato",sans-serif;font-weight:400;font-size:56px;color:var(--green);letter-spacing:-1px}

.nav{left:529px;top:104px;display:flex;height:44px;align-items:center}
.nav a{font-size:18px;color:var(--dark);text-decoration:none;padding:0 14px;line-height:44px}
.nav a.active{background:var(--green);color:#fff;padding:0 20px}

.hero{left:73px;top:183px;width:1052px;height:440px;border:4px solid var(--brown);background:linear-gradient(170deg,#e9d9a0 0%,#cdb463 45%,#9f8a2e 100%)}
.hero-title{left:520px;top:170px;width:500px;text-align:center;font-family:"Mulish",sans-serif;font-weight:800;font-size:44px;line-height:62px;color:#4f7f00}
.hero-arrow{top:200px;width:28px;height:30px;background:var(--brown)}
.hero-arrow.prev{left:-4px}
.hero-arrow.next{right:-4px}
.dots{left:548px;top:636px;display:flex;gap:4px}
.dots span{width:18px;height:18px;border-radius:50%;background:#e6e6e6;border:2px solid #bbb}
.dots span.on{background:#888}

h2{font-family:"Mulish",sans-serif;font-weight:800;color:var(--brown);font-size:31px;text-transform:uppercase;letter-spacing:-.3px}
p{font-size:14.5px;line-height:22px;color:var(--text)}
.more{font-size:14px;color:var(--green);text-decoration:none;display:inline-flex;align-items:center;gap:6px}

.services-intro{left:73px;top:686px;width:280px}
.services-intro p{margin-top:18px}
.services-intro .more{margin-top:14px}
.service-cards{left:363px;top:669px;width:764px;height:335px;background:#fff;box-shadow:0 8px 14px rgba(0,0,0,.12)}
.card{top:23px;width:238px}
.card .photo{width:238px;height:156px}
.card h3{font-size:14.5px;font-weight:400;color:var(--brown);margin:18px 0 6px}
.card .more{margin-top:14px}

.feature{top:1066px;width:240px}
.feature h2{font-size:28px}
.feature p{margin-top:18px}
.feature .more{margin-top:16px}
.divider{left:73px;top:1340px;width:1052px;height:10px;background:radial-gradient(ellipse at top,rgba(0,0,0,.12),transparent 70%)}

.clients-title{left:92px;top:1406px}
.client{top:1484px;width:154px;text-align:center}
.avatar{width:154px;height:154px;border-radius:50%;border:4px solid #fff;box-shadow:0 2px 6px rgba(0,0,0,.3)}
.client-name{margin-top:22px;font-style:italic;font-size:14px;line-height:22px;color:var(--green)}
.client-arrow{top:1541px;width:40px;height:40px;border-radius:50%;background:#d9b9a2}

.footer{left:70px;top:1781px;width:1055px;height:353px;background:var(--green)}
.footer h4{font-weight:400;font-size:17px;color:#fff;text-transform:uppercase;margin-bottom:14px}
.footer li{list-style:none;font-size:14px;line-height:22px;color:#fff}
.fcol{top:28px}
.news-item{font-size:14px;color:#fff;line-height:20px;margin-bottom:8px}
.news-item small{display:block;font-size:12px}
.footer-rule{left:0;top:278px;width:1055px;height:1px;background:rgba(255,255,255,.45)}
.copyright{left:26px;top:300px;font-size:13.5px;color:#fff}
.social{left:826px;top:296px;display:flex;gap:11px}
.social span{width:30px;height:30px;border-radius:50%;background:var(--dark)}
</style>
</head>
<body>
<div class="abs sky"></div>
<div class="abs grass left" role="img" aria-label="Tall green grass blades"></div>
<div class="abs grass right" role="img" aria-label="Tall green grass blades"></div>

<div class="abs page"></div>

<header>
  <div class="abs brand">
    <div class="brand-mark"></div>
    <div class="brand-name">FieldNorth</div>
  </div>
  <nav class="abs nav">
    <a class="active" href="#">Home</a><a href="#">About</a><a href="#">Services</a><a href="#">Events</a><a href="#">Clients</a><a href="#">Career</a><a href="#">Contact</a>
  </nav>
</header>

<section class="abs hero" role="img" aria-label="Cupped hands holding wheat ears above a golden wheat field">
  <div class="abs hero-title">BE THE LEADER IN<br>THE FIELD</div>
  <svg class="abs hero-arrow prev" viewBox="0 0 28 30"><path d="M17 9 L10 15 L17 21 Z" fill="#fff"/></svg>
  <svg class="abs hero-arrow next" viewBox="0 0 28 30"><path d="M11 9 L18 15 L11 21 Z" fill="#fff"/></svg>
</section>
<div class="abs dots"><span class="on"></span><span class="on"></span><span></span><span></span><span></span></div>

<section class="abs services-intro">
  <h2>Our Services</h2>
  <p>Lorem ipsum dolor sit amet concttur adipiscing elit. Aenean eleifend vel massa id dictum. Nulla dignissim felis tempor consequat varius erat urna vehicula nisl non volutpa.</p>
  <a class="more" href="#">View More Services <svg width="18" height="8" viewBox="0 0 18 8"><path d="M0 4H16M13 1L16 4L13 7" stroke="#5f9b00" fill="none"/></svg></a>
</section>

<section class="abs service-cards">
  <article class="abs card" style="left:27px">
    <div class="photo" role="img" aria-label="Close-up of agricultural grain seeds" style="background:linear-gradient(135deg,#c99a63,#8a5a2b)"></div>
    <h3>Agricultural Seeds</h3>
    <p>Lorem ipsum dolor sit amet con-secttur adipiscing elit. Aenean eleifend vel</p>
    <a class="more" href="#">Read More <svg width="18" height="8" viewBox="0 0 18 8"><path d="M0 4H16M13 1L16 4L13 7" stroke="#5f9b00" fill="none"/></svg></a>
  </article>
  <article class="abs card" style="left:276px">
    <div class="photo" role="img" aria-label="Tractor cultivating a ploughed field" style="background:linear-gradient(180deg,#a9c9e6 0%,#b8a48a 40%,#8a5f3e 100%)"></div>
    <h3>Weed Control Products</h3>
    <p>Lorem ipsum dolor sit amet con-secttur adipiscing elit. Aenean eleifend vel</p>
    <a class="more" href="#">Read More <svg width="18" height="8" viewBox="0 0 18 8"><path d="M0 4H16M13 1L16 4L13 7" stroke="#5f9b00" fill="none"/></svg></a>
  </article>
  <article class="abs card" style="left:524px">
    <div class="photo" role="img" aria-label="Sunflower in bloom against green foliage" style="background:radial-gradient(circle at 65% 40%,#f2c200 0%,#d9a400 22%,#6fa83a 45%,#3f7d22 100%)"></div>
    <h3>Industrial products seeds</h3>
    <p>Lorem ipsum dolor sit amet con-secttur adipiscing elit. Aenean eleifend vel</p>
    <a class="more" href="#">Read More <svg width="18" height="8" viewBox="0 0 18 8"><path d="M0 4H16M13 1L16 4L13 7" stroke="#5f9b00" fill="none"/></svg></a>
  </article>
</section>

<section class="abs feature" style="left:73px">
  <h2>About Us</h2>
  <p>Lorem ipsum dolor sit amet concttur adipiscing elit. Aenean eleifend vel massa id dictum. Nulla dignissim felis tempor consequat varius erat urna vehicula nisl non volutpa.</p>
  <a class="more" href="#">Read More <svg width="18" height="8" viewBox="0 0 18 8"><path d="M0 4H16M13 1L16 4L13 7" stroke="#5f9b00" fill="none"/></svg></a>
</section>
<section class="abs feature" style="left:343px">
  <h2>Why Choose Us</h2>
  <p>Lorem ipsum dolor sit amet concttur adipiscing elit. Aenean eleifend vel massa id dictum. Nulla dignissim felis tempor consequat varius erat urna vehicula nisl</p>
  <a class="more" href="#">Read More <svg width="18" height="8" viewBox="0 0 18 8"><path d="M0 4H16M13 1L16 4L13 7" stroke="#5f9b00" fill="none"/></svg></a>
</section>
<section class="abs feature" style="left:614px">
  <h2>Development</h2>
  <p>Lorem ipsum dolor sit amet concttur adipiscing elit. Aenean eleifend vel massa id dictum. Nulla dignissim felis tempor consequat varius erat urna vehicula nisl non volutpa.</p>
  <a class="more" href="#">Read More <svg width="18" height="8" viewBox="0 0 18 8"><path d="M0 4H16M13 1L16 4L13 7" stroke="#5f9b00" fill="none"/></svg></a>
</section>
<section class="abs feature" style="left:883px">
  <h2>Did You Know</h2>
  <p>Lorem ipsum dolor sit amet concttur adipiscing elit. Aenean eleifend vel massa id dictum. Nulla dignissim felis tempor consequat varius erat urna vehicula nisl non</p>
  <a class="more" href="#">Read More <svg width="18" height="8" viewBox="0 0 18 8"><path d="M0 4H16M13 1L16 4L13 7" stroke="#5f9b00" fill="none"/></svg></a>
</section>
<div class="abs divider"></div>

<h2 class="abs clients-title">Our Clients</h2>
<svg class="abs client-arrow" style="left:101px" viewBox="0 0 40 40"><path d="M23 13 L16 20 L23 27" stroke="#fff" stroke-width="3" fill="none"/></svg>
<svg class="abs client-arrow" style="left:1057px" viewBox="0 0 40 40"><path d="M17 13 L24 20 L17 27" stroke="#fff" stroke-width="3" fill="none"/></svg>
<div class="abs client" style="left:156px"><div class="avatar" role="img" aria-label="Portrait of farmer client" style="background:linear-gradient(180deg,#9cc86a,#5d8a3a)"></div><div class="client-name">Tom Harlow,<br>farmer, Australia</div></div>
<div class="abs client" style="left:340px"><div class="avatar" role="img" aria-label="Portrait of farmer client" style="background:linear-gradient(180deg,#8fb35a,#4f6e2c)"></div><div class="client-name">Ned Calloway,<br>farmer, England</div></div>
<div class="abs client" style="left:524px"><div class="avatar" role="img" aria-label="Farmer client tending crops" style="background:linear-gradient(180deg,#7fb04a,#3f6d22)"></div><div class="client-name">Mira Dunn,<br>farmer, Asia</div></div>
<div class="abs client" style="left:707px"><div class="avatar" role="img" aria-label="Portrait of farmer client" style="background:linear-gradient(180deg,#b6c7d4,#7a6a52)"></div><div class="client-name">Pavel Orin,<br>farmer, Myanmar</div></div>
<div class="abs client" style="left:890px"><div class="avatar" role="img" aria-label="Portrait of farmer client" style="background:linear-gradient(180deg,#c9dfee,#5a6f94)"></div><div class="client-name">Lin Sato,<br>farmer, China</div></div>

<footer class="abs footer">
  <div class="abs fcol" style="left:36px">
    <h4>Information</h4>
    <ul><li>About Us</li><li>Services</li><li>Career</li><li>Contacts</li><li>Blog</li></ul>
  </div>
  <div class="abs fcol" style="left:298px">
    <h4>Our Offer</h4>
    <ul><li>Quisque nulla</li><li>Vestibulum libero nisl</li><li>Scelerisque eget</li><li>Vivamus eget nibh</li><li>Etiam cursus leo vel</li><li>Aenean nec eros</li><li>Primis in faucibus orci</li></ul>
  </div>
  <div class="abs fcol" style="left:474px;width:340px">
    <h4>Latest Events/News</h4>
    <div class="news-item">Lorem ipsum dolor sit amet, consectetur...<small>May 28, 2013 by admin in Cum sociis natoque penatibus</small></div>
    <div class="news-item">Lorem ipsum dolor sit amet, consectetur...<small>Mar 14, 2013 by admin in Lorem ipsum dolor sit amet</small></div>
    <div class="news-item">Lorem ipsum dolor sit amet, consectetur...<small>Mar 5, 2013 by admin in Mauris fermentum dictum</small></div>
  </div>
  <div class="abs fcol" style="left:839px">
    <h4>Contact</h4>
    <ul><li>FieldNorth. © 2013 Privacy policy</li><li>42 Wattle Lane</li><li>Sydney, NSW 2000</li><li>Freephone: +1 800 555 0142</li><li>Telephone: +1 959 555 0187</li><li>FAX: + 1 504 555 0163</li><li>Email: info@fieldnorth.com</li></ul>
  </div>
  <div class="abs footer-rule"></div>
  <div class="abs copyright">© copyright 2013, all rights reserved, fieldnorth</div>
  <div class="abs social" aria-label="Social links"><span></span><span></span><span></span><span></span></div>
</footer>
</body>
</html>
```